Charity website needing new website design

Hi there. We are looking to get a revamped website for our non for profit charity. We specialise in eye cataract surgeries and ear care around the world. Please visit our website brightpathrelief.org.au for the current layout.
I have attached a brief with photos. The about us page please include an interactive map showing our locations we operate in. The website should be easy to use, match our logo design and be clear to navigate. Pixelvault and other images can be used if they fit the scheme of the website and feel. The donation page should incorporate the gateway to receive donations. The team page should have each photo of the team member next to it. Please compare to other charity websites such as KORAMEN, Globe Harbor etc. Another website which has a lovely and easy to use scheme is tlnqaustralia.org.au
The tabs should be in the following order:
About us, Why Health? Our Team, Eye Care Programs, Ear Care Programs, Contact Us, Donate.
Please make sure the website is both compatible with mobile & computer.
The Registered Charity Logo can be at the footer of the page with details of brightpath etc

```html
<!DOCTYPE html>
<html lang="en">
<head>
<meta charset="utf-8">
<title>Brightpath Aid Foundation</title>
<link rel="stylesheet" href="https://fonts.googleapis.com/css2?family=Poppins:wght@400;500;600;700;800&display=swap">
<style>
:root{
  --navy:#0d4a66;
  --green:#3db56b;
  --olive:#6a9b2e;
  --orange:#f4a93b;
  --grey:#5e5e5e;
  --text:#2a2a2a;
  --white:#ffffff;
}
*{margin:0;padding:0;box-sizing:border-box}
html,body{width:1200px;height:3906px;overflow:hidden}
body{font-family:'Poppins',sans-serif;color:var(--text);background:var(--white);position:relative}
.abs{position:absolute}
.btn{position:absolute;display:flex;align-items:center;justify-content:center;font-weight:700;text-transform:uppercase;color:var(--white);font-size:15px;letter-spacing:.3px}
.photo{position:absolute}

/* header */
.brand{left:75px;top:22px;display:flex;align-items:center;gap:12px}
.brand-dot{width:56px;height:56px;border-radius:50%;background:var(--green)}
.brand-name{font-weight:700;color:var(--navy);font-size:28px;line-height:1.05;letter-spacing:1px}
.header-donate{left:927px;top:29px;width:199px;height:56px;background:var(--olive);font-size:22px}
.nav{left:0;top:108px;width:1200px;height:66px;background:var(--navy);display:flex;align-items:center;padding-left:85px;gap:46px}
.nav a{color:var(--white);text-decoration:none;font-weight:600;font-size:15px;text-transform:uppercase}

/* hero */
.hero-photo{left:0;top:174px;width:1200px;height:584px;background:linear-gradient(90deg,#a6aaab 0%,#9ea2a2 40%,#7b7366 70%,#5a5048 100%)}
.hero-title{left:75px;top:300px;width:600px;font-weight:800;color:var(--navy);font-size:41px;line-height:42px;text-transform:uppercase}
.hero-copy{left:75px;top:440px;width:530px;color:var(--white);font-size:18px;line-height:28px;font-weight:500}
.hero-donate{left:75px;top:578px;width:167px;height:46px;background:var(--olive)}
.hero-learn{left:255px;top:578px;width:165px;height:46px;background:var(--orange)}
.donate-band{left:75px;top:695px;width:1051px;height:127px;background:var(--green);box-shadow:0 6px 14px rgba(0,0,0,.2)}
.donate-band h2{position:absolute;left:33px;top:36px;color:var(--white);font-weight:800;font-size:42px;line-height:54px}
.amount{top:42px;width:197px;height:47px;border:2px solid var(--white);font-size:28px;font-weight:800}

/* program cards */
.card-photo{top:896px;width:329px;height:276px}
.card-box{top:1140px;width:281px;height:120px;background:var(--white);box-shadow:0 4px 14px rgba(0,0,0,.15);text-align:center}
.card-box h3{font-weight:700;font-size:31px;color:#4a4a4a;margin-top:12px}
.card-box .btn{left:73px;top:64px;width:135px;height:38px;background:var(--olive);font-size:14px}

/* about */
.about-photo{left:0;top:1341px;width:587px;height:577px;background:linear-gradient(135deg,#b39b86,#8d7566 55%,#6a7ea6)}
.about-box{left:496px;top:1414px;width:630px;height:568px;background:var(--navy);color:var(--white)}
.about-box h2{position:absolute;left:29px;top:60px;font-weight:800;font-size:37px;line-height:43px;text-transform:uppercase}
.about-rule{position:absolute;left:29px;top:164px;width:102px;height:3px;background:var(--white)}
.about-box p{position:absolute;left:29px;top:182px;width:560px;font-size:15px;line-height:29px}
.about-learn{left:29px;top:451px;width:165px;height:50px;background:var(--green)}
.about-watch{left:211px;top:451px;width:166px;height:50px;border:2px solid var(--white)}

/* emergency */
.emergency{left:0;top:2060px;width:1200px;height:427px;background:var(--grey)}
.emergency-title{left:75px;top:2170px;color:var(--white);font-weight:800;font-size:38px;line-height:42px;text-transform:uppercase}
.emergency-btn{left:75px;top:2325px;width:165px;height:51px;background:var(--green)}

/* focus tiles */
.tile{width:333px;height:267px;background:linear-gradient(135deg,#f2a83a 0%,#b4b24c 50%,#3fb96c 100%);color:var(--white);text-align:center;font-weight:700;font-size:22px;line-height:33px;text-transform:uppercase}
.tile svg{position:absolute;left:50%;top:50px;transform:translateX(-50%)}
.tile span{position:absolute;left:0;right:0;top:165px}

/* newsletter */
.newsletter{left:0;top:3192px;width:1200px;height:363px;background:linear-gradient(90deg,#0d4a66,#146b78 50%,#0e5a6e)}
.newsletter h2{position:absolute;left:0;right:0;top:86px;text-align:center;color:var(--white);font-weight:800;font-size:37px}
.field{position:absolute;width:361px;height:50px;border:1.5px solid rgba(255,255,255,.8);color:var(--white);font-size:16px;padding-left:13px;display:flex;align-items:center}
.subscribe{left:602px;top:221px;width:361px;height:50px;background:var(--orange)}

/* footer */
.footer-logo{left:130px;top:3620px;width:170px;text-align:center}
.footer-logo .dot{width:56px;height:56px;border-radius:50%;background:var(--green);margin:0 auto 10px}
.footer-logo .name{font-weight:700;color:var(--navy);font-size:20px;line-height:22px}
.footer-legal{left:90px;top:3746px;width:250px;text-align:center;font-size:14px;line-height:29px;color:#444}
.socials{left:122px;top:3818px;display:flex;gap:26px}
.socials span{width:26px;height:26px;border-radius:50%;background:#2a2a2a;display:block}
.fcol{top:3622px}
.fcol h4{font-weight:700;font-size:21px;margin-bottom:12px}
.fcol li{list-style:none;font-size:14px;line-height:37px;color:#333}
.fcol .accent{color:var(--green);font-weight:700}
</style>
</head>
<body>

<header>
  <div class="abs brand"><span class="brand-dot"></span><span class="brand-name">BRIGHTPATH AID<br>FOUNDATION</span></div>
  <a class="btn header-donate">Donate Now</a>
  <nav class="abs nav">
    <a>Home</a><a>About Us</a><a>Why Health? Our Team</a><a>Eye Care Programs</a><a>Ear Care Programs</a><a>Contact Us</a>
  </nav>
</header>

<section class="hero">
  <div class="photo hero-photo" role="img" aria-label="Health worker examining an elderly man's eyes at a clinic"></div>
  <h1 class="abs hero-title">Help bring basic health care to every person on the planet.</h1>
  <p class="abs hero-copy">Through symbiotic health programs brightpath aid foundation provides innovative solutions to Eye and Hearing Health in the developing world with an ethical professional and sustainable approach.</p>
  <a class="btn hero-donate">Donate Now</a>
  <a class="btn hero-learn">Learn More</a>
  <div class="abs donate-band">
    <h2>DONATE NOW</h2>
    <a class="btn amount" style="left:383px">$10</a>
    <a class="btn amount" style="left:600px">$25</a>
    <a class="btn amount" style="left:816px">$50</a>
  </div>
</section>

<section class="programs">
  <div class="photo card-photo" style="left:75px;background:linear-gradient(135deg,#7d6a5c,#c65a3a 55%,#3b3a3a)" role="img" aria-label="Eye care treatment for a patient"></div>
  <div class="abs card-box" style="left:99px"><h3>Eye Care</h3><a class="btn">Donate</a></div>
  <div class="photo card-photo" style="left:437px;background:linear-gradient(135deg,#e0a467,#a86a3c 50%,#5b3d2a)" role="img" aria-label="Smiling children in a village"></div>
  <div class="abs card-box" style="left:461px"><h3>Ear Care</h3><a class="btn">Donate</a></div>
  <div class="photo card-photo" style="left:798px;background:linear-gradient(135deg,#9cb29a,#3a6fa8 50%,#c89070)" role="img" aria-label="Mother with baby meeting a volunteer"></div>
  <div class="abs card-box" style="left:822px"><h3>General Health</h3><a class="btn">Donate</a></div>
</section>

<section class="about">
  <div class="photo about-photo" role="img" aria-label="Two smiling women sitting against a wall"></div>
  <div class="abs about-box">
    <h2>About Us<br>Brightpath Aid Foundation</h2>
    <span class="about-rule"></span>
    <p>Brightpath Aid Foundation is dedicated to improving and transforming the lives of people through enhanced vision and hearing health in the developing world. Our mission is to bridge the gap in access to essential eye and hearing care, ensuring that everyone, regardless of their circumstances, has the opportunity to see and hear clearly. With over 70 years of humanitarian aid across our members, we are passionate to provide innovative, sustainable, ethical and professional symbiotic solutions across multiple health programs.</p>
    <a class="btn about-learn">Learn More</a>
    <a class="btn about-watch">Watch Video</a>
  </div>
</section>

<section class="emergency-section">
  <div class="abs emergency"></div>
  <svg class="abs" style="left:555px;top:2060px" width="645" height="427" viewBox="0 0 645 427">
    <defs><linearGradient id="quake" x1="0" y1="0" x2="1" y2="1"><stop offset="0" stop-color="#8a8782"/><stop offset=".6" stop-color="#5a4f48"/><stop offset="1" stop-color="#c9c9c9"/></linearGradient></defs>
    <polygon points="145,0 645,0 645,427 12,427" fill="url(#quake)" role="img" aria-label="Collapsed buildings and an ambulance after the earthquake"/>
    <line x1="145" y1="0" x2="12" y2="427" stroke="#f4a93b" stroke-width="6"/>
  </svg>
  <h2 class="abs emergency-title">Türkiye and Syria<br>earthquake medical<br>emergency aid</h2>
  <a class="btn emergency-btn">Donate Now</a>
</section>

<section class="focus">
  <div class="abs tile" style="left:254px;top:2553px">
    <svg width="90" height="80" viewBox="0 0 90 80" fill="#fff"><rect x="30" y="6" width="30" height="28" rx="3"/><rect x="10" y="40" width="30" height="28" rx="3"/><rect x="50" y="40" width="30" height="28" rx="3"/></svg>
    <span>Health<br>&amp; Hygiene Packs</span>
  </div>
  <div class="abs tile" style="left:615px;top:2553px">
    <svg width="90" height="80" viewBox="0 0 90 80"><path d="M2 40 Q45 -5 88 40 Q45 85 2 40Z" fill="#fff"/><circle cx="45" cy="40" r="17" fill="#c4b247"/><circle cx="45" cy="40" r="10" fill="#fff"/></svg>
    <span>Cataract &amp; Hearing<br>Procedures</span>
  </div>
  <div class="abs tile" style="left:254px;top:2847px">
    <svg width="90" height="80" viewBox="0 0 90 80"><rect x="32" y="4" width="26" height="14" rx="4" fill="none" stroke="#fff" stroke-width="5"/><rect x="8" y="16" width="74" height="58" rx="8" fill="#fff"/><rect x="40" y="30" width="10" height="30" fill="#c4b247"/><rect x="30" y="40" width="30" height="10" fill="#c4b247"/></svg>
    <span>Health Education<br>&amp; Training</span>
  </div>
  <div class="abs tile" style="left:615px;top:2847px">
    <svg width="90" height="80" viewBox="0 0 90 80"><path d="M20 2 H56 L72 18 V78 H20Z" fill="#fff"/><rect x="33" y="44" width="26" height="4" fill="#c4b247"/><rect x="33" y="54" width="26" height="4" fill="#c4b247"/><rect x="33" y="64" width="26" height="4" fill="#c4b247"/></svg>
    <span>Strengthening<br>Health Systems</span>
  </div>
</section>

<section class="abs newsletter" role="img" aria-label="Health worker in a knit hat tinted in teal">
  <h2>SIGN UP TO OUR NEWSLETTER</h2>
  <div class="field" style="left:226px;top:155px">Enter Name</div>
  <div class="field" style="left:602px;top:155px">Enter Email Address</div>
  <div class="field" style="left:226px;top:221px">Subject</div>
  <a class="btn subscribe">Subscribe Now</a>
</section>

<footer>
  <div class="abs footer-logo"><div class="dot"></div><div class="name">BRIGHTPATH AID<br>FOUNDATION</div></div>
  <p class="abs footer-legal">2024© Brightpath Aid Foundation.<br>All rights reserved.</p>
  <div class="abs socials" aria-label="Social media links"><span></span><span></span><span></span><span></span></div>
  <div class="abs fcol" style="left:380px"><h4>Site Map</h4><ul><li>Home</li><li>About Us</li><li>Why Health? Our Team</li><li>Eye Care Programs</li><li>Ear Care Programs</li><li>Contact Us</li></ul></div>
  <div class="abs fcol" style="left:647px"><h4>Connect</h4><ul><li>E: info@brightpathrelief.org.au</li><li>ABN: 42 117 309 264</li></ul></div>
  <div class="abs fcol" style="left:903px"><h4>Bank Details</h4><ul><li>Meridian Coast Bank</li><li class="accent">BSB: 064518</li><li class="accent">ACC: 318260455</li></ul></div>
</footer>

</body>
</html>
```